Sign Design

We already have a logo, but would like to design 2 x signs.
Sign 1:
Dimensions 1500mm wide x 2500m high.
Information to include on sign: - Clinic name and logo (attached)
- the word "DENTIST "
- Street number (which is 348)
Phone number (which is 6153 4097)

Sign 2:
Dimensions: 800mm wide x 600mm high

```html
<!DOCTYPE html>
<html lang="en">
<head>
<meta charset="UTF-8">
<title>Kellbrook Dental Care – Signage</title>
<link rel="stylesheet" href="https://fonts.googleapis.com/css2?family=Anton&family=Inter:wght@400&family=Montserrat:wght@800;900&family=Poppins:wght@800&display=swap">
<style>
  :root {
    --green: #10b11f;
    --lime: #a0df4a;
    --pale: #dff4b0;
    --deep: #0c4a24;
    --logo-green: #17703a;
    --white: #fdfdfd;
    --stage-light: #c4c4c4;
    --stage-dark: #707070;
  }
  * { margin: 0; padding: 0; box-sizing: border-box; }
  html, body { width: 1200px; height: 858px; overflow: hidden; }
  body {
    position: relative;
    background: linear-gradient(110deg, var(--stage-light) 0%, #9a9a9a 50%, var(--stage-dark) 100%);
    font-family: "Inter", Arial, sans-serif;
  }
  .sign { position: absolute; overflow: hidden; background: var(--white); }
  .sign-backdrop { position: absolute; inset: 0; width: 100%; height: 100%; display: block; }

  /* Brand block */
  .brand { position: absolute; color: var(--logo-green); font-weight: 400; line-height: 1; }
  .brand-mark { position: absolute; border-radius: 50%; background: var(--lime); }
  .brand-name { display: block; letter-spacing: -2px; }
  .brand-sub { display: block; text-align: right; letter-spacing: -1px; }

  /* Sign 1 – tall pylon */
  .pylon { left: 104px; top: 86px; width: 412px; height: 687px; }
  .pylon .brand-mark { left: 22px; top: 128px; width: 96px; height: 96px; }
  .pylon .brand { left: 138px; top: 140px; width: 238px; }
  .pylon .brand-name { font-size: 48px; }
  .pylon .brand-sub { font-size: 28px; margin-top: 4px; margin-right: 8px; }

  .headline {
    position: absolute; left: 37px; top: 238px; width: 339px;
    font-family: "Anton", Impact, sans-serif; font-size: 108px; line-height: 1.04;
    color: var(--green); text-align: center; letter-spacing: 3px;
  }

  .phone {
    position: absolute; left: 37px; top: 347px; width: 339px; height: 59px;
    border: 1.5px solid var(--logo-green); border-radius: 30px; background: var(--pale);
    display: flex; align-items: center; padding-left: 10px; gap: 10px;
  }
  .phone-icon { width: 33px; height: 33px; flex: none; }
  .phone-number {
    font-family: "Montserrat", Arial, sans-serif; font-weight: 900; font-size: 43px;
    color: var(--deep); letter-spacing: 2px; line-height: 1;
  }

  .street-number {
    position: absolute; left: 134px; top: 414px; width: 148px; height: 273px;
  }
  .street-number svg { position: absolute; inset: 0; }
  .street-label {
    position: absolute; left: 0; top: 36px; width: 148px; text-align: center;
    font-family: "Poppins", Arial, sans-serif; font-weight: 800; font-size: 13px;
    line-height: 13px; color: var(--deep);
  }
  .street-digits {
    position: absolute; left: 0; top: 63px; width: 148px; text-align: center;
    font-family: "Poppins", Arial, sans-serif; font-weight: 800; font-size: 36px;
    line-height: 36px; color: var(--deep); letter-spacing: -1px;
  }

  /* Sign 2 – wall panel */
  .panel { left: 551px; top: 230px; width: 532px; height: 399px; }
  .panel .brand-mark { left: 42px; top: 150px; width: 112px; height: 112px; }
  .panel .brand { left: 183px; top: 163px; width: 284px; }
  .panel .brand-name { font-size: 58px; }
  .panel .brand-sub { font-size: 34px; margin-top: 4px; margin-right: 14px; }
  .web {
    position: absolute; left: 34px; top: 357px;
    font-family: "Montserrat", Arial, sans-serif; font-weight: 800; font-size: 13.5px;
    color: var(--deep); letter-spacing: 0.2px;
  }
</style>
</head>
<body>

<section class="sign pylon" aria-label="Pylon sign">
  <svg class="sign-backdrop" viewBox="0 0 780 1300" preserveAspectRatio="none" aria-hidden="true">
    <rect width="780" height="1300" fill="var(--green)"/>
    <path fill="var(--white)" d="M0,290 C20,200 70,158 116,152 C170,146 240,222 318,222 C420,222 450,84 596,84 C700,84 760,130 780,222 L780,1300 L0,1300 Z"/>
    <path fill="var(--lime)" d="M0,1300 C0,1200 50,1123 191,1123 C300,1123 340,1190 385,1230 C420,1262 445,1265 463,1265 C540,1265 610,1185 670,1185 C720,1185 770,1240 780,1300 Z"/>
  </svg>

  <span class="brand-mark" aria-hidden="true"></span>
  <div class="brand">
    <span class="brand-name">Kellbrook</span>
    <span class="brand-sub">Dental Care</span>
  </div>

  <h1 class="headline">DENTIST</h1>

  <div class="phone">
    <svg class="phone-icon" viewBox="0 0 32 32" aria-hidden="true">
      <circle cx="16" cy="16" r="16" fill="var(--deep)"/>
      <circle cx="16" cy="16" r="11.5" fill="none" stroke="var(--pale)" stroke-width="1.6"/>
      <path fill="var(--pale)" d="M11.2 9.6c.6-.5 1.4-.4 1.8.2l1.4 2.1c.4.6.3 1.3-.2 1.7l-.8.7c.6 1.5 1.7 2.8 3.1 3.7l.8-.7c.5-.4 1.2-.4 1.7 0l2 1.6c.5.5.6 1.3.1 1.8l-1 1.1c-.6.6-1.5.8-2.3.5-3.5-1.3-6.1-4.2-7.1-7.8-.2-.8 0-1.7.6-2.3z"/>
      <path fill="none" stroke="var(--pale)" stroke-width="1.2" stroke-linecap="round" d="M17 10.5a4.5 4.5 0 0 1 4 4M17.3 8a7 7 0 0 1 6.2 6.3"/>
    </svg>
    <span class="phone-number">6153 4097</span>
  </div>

  <div class="street-number">
    <svg viewBox="0 0 148 273" aria-hidden="true">
      <defs>
        <linearGradient id="pole" x1="0" x2="1">
          <stop offset="0" stop-color="#8c8c8c"/>
          <stop offset="0.5" stop-color="#f2f2f2"/>
          <stop offset="1" stop-color="#8c8c8c"/>
        </linearGradient>
      </defs>
      <rect x="70.5" y="140" width="7" height="133" fill="url(#pole)"/>
      <rect x="23" y="23" width="102" height="102" rx="13" transform="rotate(45 74 74)" fill="var(--lime)"/>
      <rect x="30" y="30" width="88" height="88" rx="9" transform="rotate(45 74 74)" fill="none" stroke="var(--deep)" stroke-width="1.6"/>
    </svg>
    <p class="street-label">Street<br>Number</p>
    <p class="street-digits">348</p>
  </div>
</section>

<section class="sign panel" aria-label="Wall panel sign">
  <svg class="sign-backdrop" viewBox="0 0 1006 755" preserveAspectRatio="none" aria-hidden="true">
    <rect width="1006" height="377" fill="var(--green)"/>
    <rect y="377" width="1006" height="378" fill="var(--lime)"/>
    <path fill="var(--white)" d="M0,335 C40,200 110,168 147,168 C250,168 330,257 412,257 C520,257 560,78 769,78 C920,78 980,150 1006,255 L1006,500 C980,590 930,677 769,677 C560,677 560,497 412,497 C300,497 230,585 147,585 C100,585 30,540 0,415 Z"/>
  </svg>

  <span class="brand-mark" aria-hidden="true"></span>
  <div class="brand">
    <span class="brand-name">Kellbrook</span>
    <span class="brand-sub">Dental Care</span>
  </div>

  <p class="web">www.kellbrookdentalcare.com.au</p>
</section>

</body>
</html>
```